Brightway Freight Biz Card and Stationary
Brightway Freight
Brightway Freight Biz Card and Stationary -
Creative Brief
Modern
Daniel Prescott
President & CEO
P.O. Box 7382 Williston, ND 58217
d.prescott@tarvo.com
keep it simple

```html
<!DOCTYPE html>
<html lang="en">
<head>
<meta charset="utf-8">
<title>Brightway Freight – Stationery</title>
<link href="https://fonts.googleapis.com/css2?family=Open+Sans:wght@400;600;700&display=swap" rel="stylesheet">
<style>
:root{
  --blue:#1f7fcf;
  --blue-dark:#0c5ea8;
  --blue-pale:#e6eef7;
  --ink:#3a3f45;
  --muted:#7b8188;
  --paper:#ffffff;
  --backdrop:#e8e5e0;
}
*{box-sizing:border-box;margin:0;padding:0}
html,body{width:1200px;height:506px;overflow:hidden;background:var(--backdrop);font-family:"Open Sans",Arial,sans-serif;color:var(--ink)}
.canvas{position:relative;width:1200px;height:506px}
.sheet{position:absolute;background:var(--paper);box-shadow:0 2px 6px rgba(0,0,0,.18)}
.brand{display:flex;align-items:center;gap:6px;font-weight:700;color:var(--blue-dark);letter-spacing:.02em;text-transform:uppercase}
.brand-dot{width:12px;height:12px;border-radius:50%;background:var(--blue)}
.brand.small{font-size:11px}
.brand.small .brand-dot{width:9px;height:9px}
.watermark{position:absolute;border-radius:50%;background:radial-gradient(circle,#dfe8f2 0%,#eef3f9 60%,rgba(255,255,255,0) 72%)}
.letterhead{top:24px;width:259px;height:452px}
.letterhead.one{left:36px}
.letterhead.two{left:312px}
.letterhead .brand{position:absolute;top:22px;left:24px;font-size:12px}
.letterhead .watermark{left:60px;top:130px;width:170px;height:220px}
.edge-bar{position:absolute;left:0;bottom:0;width:4px;height:40px;background:var(--blue)}
.footer{position:absolute;bottom:12px;left:14px;right:14px;display:flex;justify-content:space-between;font-size:4.5px;line-height:1.6;color:var(--muted)}
.footer .right{text-align:right;align-self:flex-end}
.fax-title{position:absolute;top:68px;left:20px;font-size:15px;font-weight:600;color:var(--ink)}
.fax-fields{position:absolute;top:94px;left:20px;right:20px;display:grid;grid-template-columns:1fr 1fr;column-gap:14px;row-gap:7px;font-size:4.5px;color:var(--muted)}
.fax-fields span{border-bottom:0.6px solid #9aa0a6;padding-bottom:1px}
.fax-rule{position:absolute;top:148px;left:20px;right:20px;border-top:0.8px solid #9aa0a6}
.fax-checks{position:absolute;top:160px;left:20px;right:20px;display:flex;justify-content:space-between;font-size:4.5px;color:var(--muted)}
.fax-checks span::before{content:"";display:inline-block;width:5px;height:5px;border:0.6px solid #8a9096;margin-right:2px;vertical-align:-1px}
.option-label{position:absolute;top:484px;font-size:7px;color:#555}
.envelope{position:absolute;overflow:hidden}
.envelope.back{left:588px;top:53px;width:348px;height:115px}
.envelope.front{left:619px;top:163px;width:346px;height:137px}
.envelope.front .accent{position:absolute;left:14px;top:44px;width:5px;height:34px;background:var(--blue)}
.envelope.front .brand{position:absolute;left:26px;top:48px;font-size:16px}
.envelope.front .brand-dot{width:14px;height:14px}
.envelope.front .return{position:absolute;left:26px;top:74px;font-size:4.5px;color:var(--muted)}
.envelope.front .web{position:absolute;right:14px;bottom:10px;font-size:4.5px;color:var(--muted)}
.card{position:absolute;width:174px;height:104px}
.card.front{left:600px;top:350px}
.card.front .brand{position:absolute;left:10px;top:12px}
.card.front .person{position:absolute;right:10px;top:46px;text-align:right}
.person .name{font-size:7.5px;font-weight:700;color:var(--blue-dark)}
.person .role{font-size:4.5px;color:var(--muted)}
.card.front .contact{position:absolute;left:10px;top:46px;font-size:4.2px;line-height:1.65;color:var(--muted)}
.card.front .stripe{position:absolute;left:0;right:0;bottom:0;height:7px;background:var(--blue)}
.card.back{left:794px;top:352px;background:linear-gradient(135deg,var(--blue) 0%,var(--blue-dark) 100%);display:flex;align-items:center;justify-content:center}
.card.back .brand{color:#fff;font-size:12px}
.card.back .brand-dot{background:#fff}
</style>
</head>
<body>
<main class="canvas">

  <section class="sheet letterhead one" aria-label="Letterhead, option 1">
    <div class="brand"><span class="brand-dot"></span>Brightway Freight</div>
    <div class="watermark" role="img" aria-label="Faint pale-blue background decoration"></div>
    <span class="edge-bar"></span>
    <footer class="footer">
      <div>Phone: 701-555-0148<br>Cell: 701-555-0192<br>Fax: 701-555-0176<br>Email: d.prescott@tarvo.com<br>Web: www.tarvo.com</div>
      <div class="right">P.O. Box 7382<br>Williston, ND 58217</div>
    </footer>
  </section>
  <p class="option-label" style="left:150px">Option 1</p>

  <section class="sheet letterhead two" aria-label="Fax sheet, option 2">
    <div class="brand"><span class="brand-dot"></span>Brightway Freight</div>
    <h2 class="fax-title">FAX</h2>
    <div class="fax-fields">
      <span>To:</span><span>From:</span>
      <span>Fax:</span><span>Pages:</span>
      <span>Phone:</span><span>Date:</span>
      <span>Re:</span><span>CC:</span>
    </div>
    <div class="fax-rule"></div>
    <div class="fax-checks">
      <span>Urgent</span><span>For Review</span><span>Please Comment</span><span>Please Reply</span><span>Please Recycle</span>
    </div>
    <div class="watermark" role="img" aria-label="Faint pale-blue background decoration" style="top:190px"></div>
    <footer class="footer">
      <div></div>
      <div class="right">P.O. Box 7382<br>Williston, ND 58217</div>
    </footer>
  </section>
  <p class="option-label" style="left:426px">Option 2</p>

  <section class="sheet envelope back" aria-label="Envelope back">
    <svg width="348" height="115" viewBox="0 0 348 115">
      <defs>
        <linearGradient id="flapBlue" x1="0" y1="0" x2="0" y2="1">
          <stop offset="0" stop-color="#0c5ea8"/><stop offset="1" stop-color="#1f7fcf"/>
        </linearGradient>
      </defs>
      <polygon points="0,0 348,0 174,48" fill="url(#flapBlue)"/>
      <polyline points="0,115 150,62 198,62 348,115" fill="none" stroke="#d3d7dc" stroke-width="1"/>
    </svg>
  </section>

  <section class="sheet envelope front" aria-label="Envelope front">
    <span class="accent"></span>
    <div class="brand"><span class="brand-dot"></span>Brightway Freight</div>
    <p class="return">P.O. Box 7382 Williston, ND 58217</p>
    <p class="web">www.tarvo.com</p>
  </section>

  <section class="sheet card front" aria-label="Business card front">
    <div class="brand small"><span class="brand-dot"></span>Brightway Freight</div>
    <div class="contact">Phone: 701-555-0148<br>Cell: 701-555-0192<br>d.prescott@tarvo.com<br>www.tarvo.com</div>
    <div class="person">
      <p class="name">Daniel Prescott</p>
      <p class="role">President &amp; CEO</p>
    </div>
    <span class="stripe"></span>
  </section>

  <section class="sheet card back" aria-label="Business card back">
    <div class="brand"><span class="brand-dot"></span>Brightway Freight</div>
  </section>

</main>
</body>
</html>
```